Grill & Ale Room requires web site design - Casual restaurant

Need website designed for re-branding of Restaurant based in Fort Morgan, Colorado. We offer a wide variety of American cuisine in a casual, rustic atmosphere. We're offering 16 craft beers on draft, as well as a full service bar, and modern, interesting menu selections in a friendly, fun and energetic environment, with an emphasis on superior customer service and high quality, locally sourced food. We are a family, and community service oriented establishment. The website design should convey a welcoming sense, "simplicity", yet sophisticated - without pretentiousness. The website should effectively convey our "home style" relaxed atmosphere, as well as our casual character.

Business Hours: Sunday - Thursday, 11am-10pm / Friday & Saturday, 11am-11am

The Rook Grill & Ale Room
2276 Kettering Lane
Fort Morgan, Colorado 80701
B: (970) 555-0174

WEBSITE ADDRESS: therookaleroom.example

Reason: Continuing to refine top submissions.

Reason: Submissions are still accepted, while refining several potential designs.

Target Market(s)

Young Adults
Families
Blue and White Collar Americans
Senior Citizens
Small town location, appeal to everyone

Industry/Entity Type

American Restaurant

Contact Information for Business Card

Dale L Ferris
Food & Beverage Director
2276 Kettering Lane
B: (970) 555-0174
M: (231) 555-0196
dlferris@rookaleroom.example
www.therookaleroom.example
***Use logo in uploaded files
***Open to single OR double sided
*** I will have additional names and information to add to this, for other employees.

Coding

Coded - Design and coding required

Number of Pages Required

5+ page

Font styles to use
Serif
Sans Serif
Decorative
Other font styles liked:
• Calafornian FB,

Requirements
Must have
• Home/Welcome Page
• Menu Page/Online Ordering Ready
• About Us/Contact Us page
• Catering/Private Events/Banquets Advertising section
• Ability to link to Friendpage/TrailNotes/Chowlist/Instagram etc.
• Logo uploaded, reference for colors as well.
Nice to have
• About craft beer page
• Our Story/Bio section
• Photo Gallery
• Employment/Apply section
Should not have
• We are NOT a "fine dining" restaurant... think casual...

```html
<!DOCTYPE html>
<html lang="en">
<head>
<meta charset="utf-8">
<title>The Rook Grill &amp; Ale Room — Welcome</title>
<link rel="stylesheet" href="https://fonts.googleapis.com/css2?family=Great+Vibes&family=Lato:wght@400;700&family=Playfair+Display:ital@1&display=swap">
<style>
  :root {
    --gold: #c8a96e;
    --gold-soft: #b89a64;
    --white: #ffffff;
    --line-light: rgba(255,255,255,0.75);
    --nav-rule: #e6dccb;
    --ink: #1d1d1d;
    --page: #ffffff;
    --room-dark: #15100c;
    --room-mid: #3a2c20;
    --room-warm: #5b4633;
  }
  * { margin: 0; padding: 0; box-sizing: border-box; }
  html, body { width: 1200px; height: 525px; overflow: hidden; background: var(--page); }
  body { position: relative; font-family: "Lato", Arial, sans-serif; }

  .hero { position: absolute; left: 0; top: 0; width: 1200px; height: 391px; overflow: hidden; }
  .hero-backdrop {
    position: absolute; inset: 0;
    background:
      radial-gradient(ellipse 320px 200px at 600px 110px, rgba(60,80,45,0.55), transparent 70%),
      radial-gradient(ellipse 700px 160px at 600px 360px, rgba(200,190,175,0.35), transparent 70%),
      linear-gradient(90deg, var(--room-dark) 0%, var(--room-mid) 30%, var(--room-warm) 50%, var(--room-mid) 70%, var(--room-dark) 100%);
  }
  .hero-shade { position: absolute; inset: 0; background: rgba(0,0,0,0.28); }

  .slide-count {
    position: absolute; left: 90px; top: 63px; width: 88px; padding-bottom: 10px;
    border-bottom: 1px solid var(--line-light);
    font-family: "Playfair Display", Georgia, serif; font-style: italic;
    color: var(--white); font-size: 16px; text-align: center; letter-spacing: 2px;
  }
  .slide-arrow { position: absolute; top: 188px; width: 82px; height: 14px; }
  .slide-arrow.prev { left: 34px; }
  .slide-arrow.next { left: 1085px; }

  .welcome-title {
    position: absolute; left: 0; width: 1200px; top: 58px; text-align: center;
    font-family: "Great Vibes", cursive; font-weight: 400;
    font-size: 132px; line-height: 1; color: var(--gold);
  }
  .welcome-tagline {
    position: absolute; left: 0; width: 1200px; top: 230px; text-align: center;
    font-size: 17px; letter-spacing: 5px; color: var(--gold-soft);
  }
  .reserve-button {
    position: absolute; left: 526px; top: 278px; width: 148px; height: 48px;
    border: 1px solid var(--line-light); display: flex; align-items: center; justify-content: center;
    color: var(--white); font-size: 14px; font-weight: 700; letter-spacing: 0.5px; text-decoration: none;
  }

  .social-links { position: absolute; left: 90px; top: 256px; list-style: none; }
  .social-links li { margin-bottom: 9px; }
  .social-links a {
    color: var(--white); font-size: 14px; text-decoration: none;
    padding-bottom: 3px; border-bottom: 1px solid rgba(255,255,255,0.55);
  }

  .contact-top { position: absolute; right: 90px; top: 54px; text-align: right; color: var(--white); font-size: 13px; line-height: 20px; }
  .contact-top a { color: var(--white); text-decoration: none; border-bottom: 1px dotted var(--white); }

  .show-picture {
    position: absolute; left: 1029px; top: 324px; font-size: 9px; font-weight: 700;
    letter-spacing: 1px; color: rgba(255,255,255,0.8);
  }

  .site-header { position: absolute; left: 0; top: 391px; width: 1200px; height: 134px; background: var(--page); }
  .brand-name { position: absolute; left: 105px; top: 34px; color: var(--ink); font-weight: 700; line-height: 1; }
  .brand-name .brand-main { display: block; font-size: 36px; letter-spacing: -0.5px; }
  .brand-name .brand-sub { display: block; font-size: 12px; margin-top: 6px; letter-spacing: 0.5px; }

  .main-nav { position: absolute; left: 529px; top: 60px; list-style: none; display: flex; }
  .main-nav li { margin-right: 37px; }
  .main-nav li:last-child { margin-right: 0; }
  .main-nav a {
    color: var(--gold); font-size: 13px; letter-spacing: 2.6px; text-decoration: none;
    padding-bottom: 5px; border-bottom: 1px solid var(--nav-rule);
  }
</style>
</head>
<body>
  <section class="hero">
    <div class="hero-backdrop" role="img" aria-label="Photo of a warmly lit dining room with set tables, a chandelier and a green plant wall"></div>
    <div class="hero-shade"></div>

    <div class="slide-count">1 &nbsp;of&nbsp; 3</div>

    <svg class="slide-arrow prev" viewBox="0 0 82 14" aria-hidden="true">
      <line x1="1" y1="7" x2="82" y2="7" stroke="#fff" stroke-opacity="0.8" stroke-width="1"/>
      <polyline points="8,1 1,7 8,13" fill="none" stroke="#fff" stroke-opacity="0.8" stroke-width="1"/>
    </svg>
    <svg class="slide-arrow next" viewBox="0 0 82 14" aria-hidden="true">
      <line x1="0" y1="7" x2="81" y2="7" stroke="#fff" stroke-opacity="0.8" stroke-width="1"/>
      <polyline points="74,1 81,7 74,13" fill="none" stroke="#fff" stroke-opacity="0.8" stroke-width="1"/>
    </svg>

    <h1 class="welcome-title">Welcome</h1>
    <p class="welcome-tagline">exclusive drinking &amp; dining</p>
    <a class="reserve-button" href="#reservation">RESERVATION</a>

    <ul class="social-links">
      <li><a href="#">Friendpage</a></li>
      <li><a href="#">TrailNotes</a></li>
      <li><a href="#">Chowlist</a></li>
    </ul>

    <div class="contact-top">
      <a href="#">hello@rookaleroom.example</a><br>
      +44 12 555 010 980
    </div>

    <div class="show-picture">SHOW PICTURE</div>
  </section>

  <header class="site-header">
    <div class="brand-name">
      <span class="brand-main">The Rook</span>
      <span class="brand-sub">Grill &amp; Ale Room</span>
    </div>
    <ul class="main-nav">
      <li><a href="#about">ABOUT</a></li>
      <li><a href="#menu">MENU</a></li>
      <li><a href="#reservation">RESERVATION</a></li>
      <li><a href="#blog">BLOG</a></li>
      <li><a href="#contact">CONTACT</a></li>
      <li><a href="#demos">DEMOS</a></li>
    </ul>
  </header>
</body>
</html>
```